Welding Fabrication and Inspection Business Card Design

Welding Fabrication and Inspection Services,

Business

Industrial Machinery ServicesMohammed Rahim30 Ballarat Street, Mount Gravatt East.4122.QLD

```html
<!DOCTYPE html>
<html lang="en">
<head>
<meta charset="utf-8">
<title>Corvane Plant Services – Business Card</title>
<link rel="stylesheet" href="https://fonts.googleapis.com/css2?family=PT+Sans:ital,wght@0,400;0,700;1,400&display=swap">
<style>
  :root {
    --stage: #e9e9e9;
    --card-white: #ffffff;
    --card-dark: #2c2a2b;
    --ink: #333333;
    --ink-soft: #8a8a8a;
    --rule: #b9b9b9;
    --band: #2c2a2b;
    --band-text: #f2f2f2;
    --tool-red: #9e3a3c;
    --tool-dark: #3d4038;
  }
  * { box-sizing: border-box; margin: 0; padding: 0; }
  html, body { width: 1105px; height: 1200px; overflow: hidden; }
  body {
    background: var(--stage);
    font-family: "PT Sans", sans-serif;
    color: var(--ink);
    position: relative;
  }
  .card {
    position: absolute;
    left: 196px;
    width: 721px;
    height: 412px;
    overflow: hidden;
  }
  .card--front { top: 146px; background: var(--card-white); }
  .card--back { top: 602px; background: var(--card-dark); }

  .product-image {
    position: absolute;
    left: 57px; top: 23px;
    width: 210px; height: 162px;
    background: linear-gradient(180deg, var(--tool-red) 0%, var(--tool-red) 45%, var(--tool-dark) 46%, #5a5d52 100%);
    border-radius: 6px;
  }

  .brand {
    position: absolute;
    display: flex;
    align-items: center;
    gap: 12px;
    font-weight: 700;
    white-space: nowrap;
  }
  .brand__dot {
    width: 16px; height: 16px;
    border-radius: 50%;
    background: currentColor;
    flex: none;
  }
  .brand--front {
    right: 58px; top: 70px;
    font-size: 26px;
    color: var(--ink);
  }
  .brand--back {
    left: 0; right: 0; top: 180px;
    justify-content: center;
    font-size: 38px;
    color: var(--card-white);
  }

  .holder {
    position: absolute;
    left: 44px; top: 232px;
  }
  .holder__name { font-size: 26px; font-weight: 700; line-height: 1.2; color: var(--ink); }
  .holder__role { font-size: 19px; color: var(--ink-soft); line-height: 1.4; }
  .holder__address { font-size: 19px; line-height: 1.42; font-style: normal; }

  .contact {
    position: absolute;
    right: 58px; top: 236px;
    list-style: none;
    font-size: 19px;
    line-height: 27.5px;
    text-align: right;
  }
  .contact__item { display: flex; align-items: center; justify-content: flex-end; gap: 10px; }
  .contact__icon { width: 17px; height: 17px; fill: var(--ink); flex: none; }

  .tagline-rule {
    position: absolute;
    left: 0; right: 0; top: 372px;
    height: 5px;
    background: var(--rule);
  }
  .tagline {
    position: absolute;
    left: 0; right: 0; bottom: 0;
    height: 35px;
    background: var(--band);
    color: var(--band-text);
    font-style: italic;
    font-size: 19px;
    letter-spacing: 0.5px;
    text-align: center;
    line-height: 35px;
  }
</style>
</head>
<body>
  <section class="card card--front">
    <div class="product-image" role="img" aria-label="Photo of a red magnetic particle inspection yoke with articulated legs"></div>

    <div class="brand brand--front"><span class="brand__dot"></span>Corvane Plant Services</div>

    <div class="holder">
      <p class="holder__name">Tariq Osmani</p>
      <p class="holder__role">CEO/Founder</p>
      <address class="holder__address">17 Windorah Street<br>Kessling Ridge. 4127.QLD</address>
    </div>

    <ul class="contact">
      <li class="contact__item">482 555 0174
        <svg class="contact__icon" viewBox="0 0 24 24"><path d="M6.6 10.8a15.1 15.1 0 0 0 6.6 6.6l2.2-2.2c.3-.3.7-.4 1-.2 1.1.4 2.3.6 3.6.6.6 0 1 .4 1 1V20c0 .6-.4 1-1 1A17 17 0 0 1 3 4c0-.6.4-1 1-1h3.5c.6 0 1 .4 1 1 0 1.3.2 2.5.6 3.6.1.3 0 .7-.2 1z"/></svg>
      </li>
      <li class="contact__item">872 555 0163
        <svg class="contact__icon" viewBox="0 0 24 24"><path d="M7 1h10a2 2 0 0 1 2 2v18a2 2 0 0 1-2 2H7a2 2 0 0 1-2-2V3a2 2 0 0 1 2-2zm0 3v15h10V4z"/></svg>
      </li>
      <li class="contact__item">info@corvaneplant.com
        <svg class="contact__icon" viewBox="0 0 24 24"><path d="M2 5h20v14H2zm2 2v.5l8 5 8-5V7z"/></svg>
      </li>
      <li class="contact__item">www.corvaneplant.com
        <svg class="contact__icon" viewBox="0 0 24 24"><path d="M12 2a10 10 0 1 0 0 20 10 10 0 0 0 0-20zm-1 17.9A8 8 0 0 1 4.2 10L9 14.8v1a2 2 0 0 0 2 2zm6.9-2.5a2 2 0 0 0-1.9-1.4h-1v-3a1 1 0 0 0-1-1H8v-2h2a1 1 0 0 0 1-1V7h2a2 2 0 0 0 2-2v-.4a8 8 0 0 1 2.9 12.8z"/></svg>
      </li>
    </ul>

    <div class="tagline-rule"></div>
    <p class="tagline">Welding Fabrication &amp; Inspection Services</p>
  </section>

  <section class="card card--back">
    <div class="brand brand--back"><span class="brand__dot"></span>Corvane Plant Services</div>
  </section>
</body>
</html>
```